Nera Bloom Fitness Coaching Project

I am a personal trainer based in London. My services include one-on-one PT sessions, bootcamps.
I would like the design to be minimalistic. With light colours: white, pink, purple.
I specialise in weight loss, flexibility, mobility.

Orla Pemvick
Personal Trainer
Email: orla.pemvick@tovamail.com
tel: 07400918243
Instagram: Nera Bloom

Target Market(s)

adults, mostly females (age 18-50).

Industry/Entity Type

Fitness

Contact Information for Business Card

Orla Pemvick
Personal Trainer
tel: 07400918243
Instagram: Nera Bloom

Font styles to use
Serif

Colors
eea4c8
fbd4d5
fdf9cf
cfeae6
cee9f5

Requirements
Nice to have
• minimalistic style
• easy to read and remember

```html
<!DOCTYPE html>
<html lang="en">
<head>
<meta charset="utf-8">
<title>Nera Bloom Fitness Coaching – Business Card</title>
<link href="https://fonts.googleapis.com/css2?family=Cinzel:wght@400;500&family=Open+Sans:wght@400;700&display=swap" rel="stylesheet">
<style>
  :root {
    --backdrop: #3b3430;
    --card: #0c0c0c;
    --silver: #c4c4c4;
    --white: #f2f2f2;
    --muted: #a9a9a9;
  }
  * { box-sizing: border-box; margin: 0; padding: 0; }
  html, body {
    width: 1200px; height: 900px; overflow: hidden;
    background: var(--backdrop);
    font-family: "Open Sans", Arial, sans-serif;
  }
  .stage {
    position: relative; width: 1200px; height: 900px;
    display: flex; align-items: center; justify-content: center; gap: 50px;
  }
  .card {
    position: relative;
    width: 520px; height: 310px;
    background: var(--card);
    border-radius: 4px;
    box-shadow: 0 14px 30px rgba(0,0,0,.45);
    color: var(--white);
  }

  /* Emblem: plain ring with the brand name */
  .emblem { display: flex; flex-direction: column; align-items: center; gap: 8px; }
  .emblem-ring { border: 3px solid var(--silver); border-radius: 50%; }
  .emblem-name {
    font-family: "Open Sans", Arial, sans-serif;
    font-weight: 700; color: var(--silver);
    letter-spacing: .5px;
  }

  /* Contact side */
  .card-contact .emblem { position: absolute; left: 50px; top: 60px; }
  .card-contact .emblem-ring { width: 150px; height: 150px; }
  .card-contact .emblem-name { font-size: 16px; }
  .contact-details { position: absolute; left: 250px; top: 92px; }
  .person-name {
    font-size: 19px; font-weight: 700; letter-spacing: .5px;
    text-transform: uppercase;
  }
  .person-role { font-size: 13px; color: var(--muted); margin-bottom: 12px; }
  .contact-line {
    display: flex; align-items: center; gap: 7px;
    font-size: 13px; color: var(--silver); line-height: 20px;
  }
  .contact-line svg { width: 11px; height: 11px; fill: var(--silver); flex: none; }
  .social-line { margin-top: 18px; }
  .social-dot { width: 12px; height: 12px; border-radius: 50%; background: var(--silver); flex: none; }

  /* Brand side */
  .card-brand { display: flex; flex-direction: column; align-items: center; padding-top: 34px; }
  .card-brand .emblem-ring { width: 78px; height: 78px; }
  .card-brand .emblem-name { font-size: 12px; }
  .wordmark {
    margin-top: 14px;
    font-family: "Cinzel", Georgia, serif;
    font-weight: 500;
    font-size: 30px; letter-spacing: 1px;
    color: var(--silver);
  }
  .tagline {
    display: flex; align-items: center; gap: 12px;
    margin-top: 2px;
    font-size: 11px; letter-spacing: 4px; color: var(--muted);
  }
  .tagline-rule { width: 80px; height: 1px; background: var(--muted); }
  .specialties {
    display: flex; gap: 16px; margin-top: 14px;
    font-size: 13px; color: var(--white);
  }
  .specialties li { list-style: none; display: flex; align-items: center; gap: 6px; }
  .specialties li::before {
    content: ""; width: 6px; height: 6px; border-radius: 50%; background: var(--muted);
  }
</style>
</head>
<body>
<main class="stage">

  <section class="card card-contact">
    <div class="emblem">
      <div class="emblem-ring"></div>
      <span class="emblem-name">Nera Bloom</span>
    </div>
    <div class="contact-details">
      <h1 class="person-name">Orla Pemvick</h1>
      <p class="person-role">Personal Trainer</p>
      <p class="contact-line">
        <svg viewBox="0 0 24 24" aria-hidden="true"><path d="M6.6 10.8a15.1 15.1 0 0 0 6.6 6.6l2.2-2.2a1 1 0 0 1 1-.25 11.4 11.4 0 0 0 3.6.57 1 1 0 0 1 1 1V20a1 1 0 0 1-1 1A17 17 0 0 1 3 4a1 1 0 0 1 1-1h3.5a1 1 0 0 1 1 1c0 1.25.2 2.45.57 3.57a1 1 0 0 1-.25 1z"/></svg>
        07400918243
      </p>
      <p class="contact-line">
        <svg viewBox="0 0 24 24" aria-hidden="true"><path d="M2 5h20v14H2z M2 5l10 8 10-8"/></svg>
        orla.pemvick@tovamail.com
      </p>
      <p class="contact-line social-line">
        <span class="social-dot"></span>
        Nera Bloom
      </p>
    </div>
  </section>

  <section class="card card-brand">
    <div class="emblem">
      <div class="emblem-ring"></div>
      <span class="emblem-name">Nera Bloom</span>
    </div>
    <h2 class="wordmark">NERA BLOOM FITNESS</h2>
    <p class="tagline"><span class="tagline-rule"></span>COACHING PROJECT<span class="tagline-rule"></span></p>
    <ul class="specialties">
      <li>Weight Loss</li>
      <li>Flexibility</li>
      <li>Mobility</li>
    </ul>
  </section>

</main>
</body>
</html>
```